hair salon logo and Business Card Design

this logo needs to reflect a vibrant, trendy and fun business, targeting 20 to 50 year old ladies in a nice sunny part of Australia.Our aim is to make everyone feel in a fantastic mood when they walk out of the salon,and look equally glamorous.
I would like the logo to be simple yet using bold colors and font.
ideally the name mirra would be lowercase with a nice rounded shape and hair+beauty, with upper case and the letter i in an inverted position.

Industry/Entity Type

Hair

Contact Information for Business Card

mirra
hair | beauty.

Lia Forsett
stylist/owner
0419376052
58 Wexcombe St. Scarborough QLD. 4020

Requirements
Must have
• front all the business details
back lined for writing notes.
Nice to have
• use of bold stand out colors, simple shapes sense of movement, not stillness, modern, professional.

```html
<!DOCTYPE html>
<html lang="en">
<head>
<meta charset="utf-8">
<title>mirra hair | beauty — business card</title>
<link href="https://fonts.googleapis.com/css2?family=Montserrat:wght@300;400;600;700&display=swap" rel="stylesheet">
<style>
  :root {
    --teal: #1ba4ae;
    --teal-deep: #12868f;
    --tan: #c8ab84;
    --card: #ffffff;
    --backdrop: #e8e5e0;
  }
  * { box-sizing: border-box; margin: 0; padding: 0; }
  html, body { width: 1200px; height: 1001px; overflow: hidden; }
  body {
    background: var(--backdrop);
    font-family: "Montserrat", Arial, sans-serif;
    position: relative;
  }
  .card {
    position: absolute;
    left: 180px;
    width: 840px;
    height: 460px;
    background: var(--card);
    border-radius: 28px;
    overflow: hidden;
    box-shadow: 0 6px 18px rgba(0,0,0,0.12);
  }
  .card--front { top: 27px; }
  .card--back { top: 514px; }
  .card-shapes { position: absolute; inset: 0; width: 840px; height: 460px; }

  .portrait {
    position: absolute;
    border-radius: 46% 46% 20% 20%;
    background: linear-gradient(160deg, var(--teal) 0%, var(--teal-deep) 100%);
  }
  .brand-name {
    position: absolute;
    font-weight: 600;
    color: var(--tan);
    letter-spacing: 1px;
    line-height: 1;
  }

  /* front */
  .card--front .portrait { left: 310px; top: 32px; width: 110px; height: 124px; }
  .card--front .brand-name { left: 436px; top: 96px; font-size: 54px; }
  .person { position: absolute; left: 80px; top: 268px; color: #fff; }
  .person-name { font-size: 30px; font-weight: 700; }
  .person-role { font-size: 21px; font-weight: 400; margin-top: 8px; }
  .divider { position: absolute; left: 330px; top: 262px; width: 2px; height: 84px; background: rgba(255,255,255,0.85); }
  .contact-list { position: absolute; left: 352px; top: 262px; list-style: none; color: #fff; font-size: 20px; }
  .contact-list li { display: flex; align-items: center; gap: 12px; height: 40px; }
  .contact-icon { width: 26px; height: 26px; flex: none; }

  /* back */
  .salon-title { position: absolute; left: 120px; top: 72px; color: #fff; font-size: 42px; font-weight: 400; letter-spacing: 1px; }
  .salon-title strong { font-weight: 600; }
  .salon-title span { font-weight: 300; letter-spacing: 3px; }
  .salon-address { position: absolute; left: 120px; top: 140px; color: #fff; font-size: 22px; font-weight: 400; }
  .card--back .portrait { left: 70px; top: 262px; width: 110px; height: 124px; }
  .card--back .brand-name { left: 196px; top: 326px; font-size: 52px; }
</style>
</head>
<body>

<section class="card card--front" aria-label="Card front">
  <svg class="card-shapes" viewBox="0 0 840 460" aria-hidden="true">
    <path d="M0,262 Q420,186 840,226 L840,352 Q420,396 0,334 Z" fill="var(--teal)"/>
    <path d="M0,352 Q420,420 840,372" fill="none" stroke="var(--tan)" stroke-width="4"/>
    <path d="M0,372 Q420,438 840,392" fill="none" stroke="var(--tan)" stroke-width="1.5" opacity="0.6"/>
  </svg>

  <div class="portrait" role="img" aria-label="Illustrated portrait of a glamorous woman, brand emblem"></div>
  <div class="brand-name">mirra</div>

  <div class="person">
    <p class="person-name">Lia Forsett</p>
    <p class="person-role">stylist/owner</p>
  </div>
  <div class="divider"></div>
  <ul class="contact-list">
    <li>
      <svg class="contact-icon" viewBox="0 0 26 26" aria-hidden="true">
        <circle cx="13" cy="13" r="12" fill="#fff"/>
        <path d="M9,7 l3,0 l1,4 l-2,1 q1.5,3 4,4 l1,-2 l4,1 l0,3 q-8,1 -11,-11 z" fill="var(--teal)"/>
      </svg>
      <span>0419376052</span>
    </li>
    <li>
      <svg class="contact-icon" viewBox="0 0 26 26" aria-hidden="true">
        <circle cx="13" cy="13" r="12" fill="#fff"/>
        <rect x="7" y="9" width="12" height="8" fill="none" stroke="var(--teal)" stroke-width="1.6"/>
        <path d="M7,9 l6,5 l6,-5" fill="none" stroke="var(--teal)" stroke-width="1.6"/>
      </svg>
      <span>hello@mirrahairbeauty.com.au</span>
    </li>
  </ul>
</section>

<section class="card card--back" aria-label="Card back">
  <svg class="card-shapes" viewBox="0 0 840 460" aria-hidden="true">
    <path d="M0,40 Q420,-6 840,30 L840,196 Q420,250 0,206 Z" fill="var(--teal)"/>
    <path d="M0,224 Q420,270 840,214" fill="none" stroke="var(--tan)" stroke-width="4"/>
    <g stroke="var(--tan)" stroke-width="2">
      <line x1="440" y1="270" x2="800" y2="270"/>
      <line x1="440" y1="312" x2="800" y2="312"/>
      <line x1="440" y1="354" x2="800" y2="354"/>
      <line x1="440" y1="396" x2="800" y2="396"/>
    </g>
  </svg>

  <p class="salon-title"><strong>mirra</strong> <span>HAIR | BEAUTY</span></p>
  <p class="salon-address">58 Wexcombe St. Tallowbay Cove 4517</p>

  <div class="portrait" role="img" aria-label="Illustrated portrait of a glamorous woman, brand emblem"></div>
  <div class="brand-name">mirra</div>
</section>

</body>
</html>
```